Crafting the Quiet Harbor *

Bold eye-catching design for business non-fiction: I am seeking a bold, and clean design for a book. The book will be 6X9 for both the ebook and in print. I am open to ideas, but found that books like “warm by winter” with contrast are highly desirable for business books.

I am open to color choices.

I would also like a growth orientated graphic in the book - something to show growth, leadership, movement. Not just a plain graphic.

The title:

Crafting the Quiet Harbor

The subtitle - I am open to suggestions. Two subtitles I am considering:

A framework for new sales leaders and those who want to keep winning.

A guide for new sales leaders and those who want to keep winning.

The below is an introduction of the book: (Back Jacket)

Sales transformation is a topic that is infrequently written about. For the new sales leader, there are a myriad of books written on coaching, leadership, forecasting, solution selling and sales process but very little is written about how to assess a sales team and build a plan for long-term success.

Through my sales leadership career, whether recently promoted or starting with a new team, I have often asked the question: Where do I start?

In the end, I was disappointed with the answers from currently available books and research, left to figure it out myself - which I did over a decade, with great pain and through many transformations. The inability to answer the question – Where do I start? – is why I wrote this book. To answer that question.

The goal of this book is to help sales leaders answer that question by providing a framework to understand the business, build a plan, and guide the team through the different stages of a sales transformation. A framework to succeed at the fastest pace possible, quarter after quarter.

(End back jacket - the rest is just additional context)

Over the last decade, I have had the privilege of leading teams in North America, Europe, and Asia. I have led turnarounds, growth businesses, and realignments. Each team was different in size, complexity, and culture; and each one offered up new and unique challenges. Each team operated with different market dynamics: one was a commodity; one was a low-cost leader; one was a market innovator. Each transformation helped me learn by taking risks, by failing and by succeeding. At each step, I had many teachers; and as I learned, I made notes. Over time I built a framework that you can leverage as you read and absorb this book. As you lead your team through a sales transformation.

I hope that this book will become for you what The Lantern Hours is for me: a favorite on your bookshelf; underlined, highlighted, dog-eared, and an ongoing reference.

Sales leadership is a journey. It is never linear, and it is always changing. At different times, different parts of this book will apply, while others will not, but hopefully, you will find it a useful and long-lasting reference.

Target Market(s)

Business readers. Sales leaders.

Requirements
Must have
• Modern, clear, eye catching colours. Clean. Graphics that indicate growth, leadership, strength.
• Please ensure the design has the full cover and back jacket design. Please use the introduction of the book as the back jacket text.

```html
<!DOCTYPE html>
<html lang="en">
<head>
<meta charset="utf-8">
<title>Crafting the Quiet Harbor — Cover Spread</title>
<link rel="stylesheet" href="https://fonts.googleapis.com/css2?family=Ubuntu:wght@400;500&display=swap">
<style>
  :root {
    --stage: #efeff1;
    --paper: #f1f1f3;
    --red: #ec5238;
    --green: #4f9b74;
    --white: #ffffff;
    --orange: #f6a33a;
    --yellow: #f2cf4a;
    --lime: #b8cc4e;
  }
  * { margin: 0; padding: 0; box-sizing: border-box; }
  html, body {
    width: 1200px; height: 1200px; overflow: hidden;
    background: var(--stage);
    font-family: "Ubuntu", sans-serif;
  }
  .spread {
    position: absolute; left: 54px; top: 223px;
    width: 1094px; height: 753px;
    background: var(--paper);
  }
  /* back panel */
  .back-author {
    position: absolute; left: 0; width: 500px; top: 56px;
    text-align: center; color: var(--red);
    font-weight: 500; font-size: 27px; letter-spacing: 0.5px;
  }
  .back-title {
    position: absolute; left: 0; width: 500px; top: 98px;
    text-align: center; color: var(--green);
    font-weight: 500; font-size: 39px; line-height: 47px; letter-spacing: 1px;
  }
  .back-copy {
    position: absolute; left: 30px; top: 236px; width: 441px;
    color: var(--red); font-size: 17.4px; line-height: 17.3px;
    text-align: justify; hyphens: auto;
  }
  .back-copy p + p { margin-top: 17px; }
  /* spine */
  .spine {
    position: absolute; left: 586px; top: 20px; height: 720px; width: 30px;
    writing-mode: vertical-rl;
    font-size: 20px; letter-spacing: 1px; word-spacing: 14px;
    white-space: nowrap;
  }
  .spine-title { color: var(--red); }
  .spine-author { color: var(--green); margin-top: 20px; }
  /* front panel */
  .front {
    position: absolute; left: 590px; top: 0; width: 504px; height: 753px;
  }
  .front-title {
    position: absolute; left: 0; width: 504px; top: 28px;
    text-align: center; color: var(--red); font-weight: 500;
  }
  .title-line-1 { font-size: 84px; line-height: 84px; letter-spacing: 2px; }
  .title-joiner {
    display: flex; align-items: center; justify-content: center; gap: 14px;
    font-size: 44px; line-height: 44px; margin-top: -4px;
  }
  .title-joiner .rule { display: block; width: 112px; height: 5px; background: var(--red); }
  .title-line-3 { font-size: 108px; line-height: 106px; letter-spacing: 2px; }
  .title-line-4 { font-size: 40px; line-height: 44px; letter-spacing: 1px; }
  .subtitle {
    position: absolute; left: 0; width: 504px; top: 302px;
    text-align: center; color: var(--green);
    font-size: 17.5px; line-height: 22px; letter-spacing: 0.3px;
  }
  .growth-art {
    position: absolute; left: 0; bottom: 0; width: 504px; height: 370px;
    background:
      linear-gradient(to top, rgba(236,82,56,0.95) 0%, rgba(246,163,58,0.75) 30%, rgba(79,155,116,0.35) 62%, rgba(241,241,243,0) 100%);
  }
  .front-author {
    position: absolute; left: 0; width: 504px; bottom: 30px;
    text-align: center; color: var(--white);
    font-weight: 500; font-size: 20px; line-height: 25px; letter-spacing: 0.5px;
  }
</style>
</head>
<body>
  <div class="spread">
    <section class="back-panel">
      <div class="back-author">DANIEL HARROW</div>
      <h2 class="back-title">CRAFTING THE<br>QUIET HARBOR</h2>
      <div class="back-copy">
        <p>Sales transformation is a topic that is infrequently written about. For the new sales leader, there are a myriad of books written on coaching, leadership, forecasting, solution selling and sales process but very little is written about how to assess a sales team and build a plan for long-term success.</p>
        <p>Through my sales leadership career, whether recently promoted or starting with a new team, I have often asked the question: Where do I start?</p>
        <p>In the end, I was disappointed with the answers from currently available books and research, left to figure it out myself - which I did over a decade, with great pain and through many transformations. The inability to answer the question – Where do I start? – is why I wrote this book. To answer that question.</p>
        <p>The goal of this book is to help sales leaders answer that question by providing a framework to understand the business, build a plan, and guide the team through the different stages of a sales transformation. A framework to succeed at the fastest pace possible, quarter after quarter.</p>
      </div>
    </section>

    <div class="spine">
      <span class="spine-title">CRAFTING THE QUIET HARBOR</span>
      <span class="spine-author">DANIEL HARROW</span>
    </div>

    <section class="front">
      <h1 class="front-title">
        <div class="title-line-1">CRAFTING</div>
        <div class="title-joiner"><span class="rule"></span>THE<span class="rule"></span></div>
        <div class="title-line-3">QUIET</div>
        <div class="title-line-4">HARBOR</div>
      </h1>
      <p class="subtitle">A FRAMEWORK FOR NEW<br>SALES LEADERS AND THOSE<br>WHO WANT TO KEEP WINNING</p>
      <div class="growth-art" role="img" aria-label="Illustration of colourful upward arrows rising from road lanes into clouds, symbolising growth"></div>
      <div class="front-author">DANIEL<br>HARROW</div>
    </section>
  </div>
</body>
</html>
```